I need a business card design for my new clinic (SPORTS MEDICINE OF KNEE). I am orthopedist, expert in sports surgery, especially knee surgery. I prefer, as colors, the colors of my logo (green, black and white). I already have my logo and should appear on my card. It's good to see my site to have ideas (www.drlucianovarela.com)
It needs contain:
my name: Dr. Luciano Varela
my registration: CRM 584-902
my specialty: Cirurgia do Joelho / Esporte
my address: Centro Executivo - Pinheiral Plaza
Av. Doutor Augusto Brandão Cunha, 2740 sala 0836
Jd. Ipanema - Ribeirão Preto - SP
my phone number: Tel (16) 8245-3908
my clinic phone: (16) 3670-4851
my e-mail: drlucianovarela@mailbox-exemplo.com
my site: www.drlucianovarela.com

Target Market(s)

futures patients

Industry/Entity Type

Clinic

Requirements
Nice to have
• letters not overfilled
straight lines, with few curves

```html
<!DOCTYPE html>
<html lang="pt-BR">
<head>
<meta charset="utf-8">
<title>Varela – Cartão de Visita</title>
<link rel="stylesheet" href="https://fonts.googleapis.com/css2?family=Noto+Sans:wght@400&family=Old+Standard+TT:wght@400&display=swap">
<style>
  :root {
    --card-black: #231f20;
    --brand-green: #43bb7a;
    --tagline-green: #1f9a4e;
    --white: #ffffff;
    --page: #ffffff;
  }
  * { margin: 0; padding: 0; box-sizing: border-box; }
  html, body {
    width: 776px;
    height: 1200px;
    overflow: hidden;
    background: var(--page);
  }
  .card {
    position: relative;
    width: 776px;
    height: 1200px;
    background: var(--card-black);
    border-radius: 48px;
    overflow: hidden;
    font-family: "Noto Sans", Verdana, sans-serif;
    color: var(--white);
  }
  .brand-square {
    position: absolute;
    left: 50px;
    top: 66px;
    width: 194px;
    height: 180px;
    border: 5px solid var(--white);
    border-radius: 14px;
    background: var(--brand-green);
  }
  .brand-name {
    position: absolute;
    left: 292px;
    top: 78px;
    width: 440px;
    text-align: center;
    font-size: 98px;
    line-height: 1;
    font-weight: 400;
    letter-spacing: 3px;
    color: var(--white);
  }
  .brand-tagline {
    position: absolute;
    left: 292px;
    top: 186px;
    width: 440px;
    text-align: center;
    font-family: "Old Standard TT", "Century Schoolbook", serif;
    font-size: 34px;
    line-height: 1;
    color: var(--tagline-green);
  }
  .stripe {
    position: absolute;
    left: 0;
    width: 100%;
    height: 7px;
    background: var(--brand-green);
  }
  .stripe--1 { top: 385px; }
  .stripe--2 { top: 407px; }
  .stripe--3 { top: 640px; }
  .stripe--4 { top: 659px; }
  .name-band {
    position: absolute;
    left: 0;
    top: 434px;
    width: 100%;
    height: 184px;
    background: var(--brand-green);
    display: flex;
    flex-direction: column;
    justify-content: center;
    align-items: center;
    font-size: 31px;
    line-height: 42px;
    text-align: center;
  }
  .contact {
    position: absolute;
    left: 0;
    top: 810px;
    width: 100%;
    text-align: center;
    font-size: 22.5px;
    line-height: 30px;
  }
  .contact__web {
    display: flex;
    justify-content: center;
    gap: 28px;
    font-size: 19.5px;
    margin-top: 2px;
  }
  .contact__phones {
    display: grid;
    grid-template-columns: 209px auto;
    width: 440px;
    margin: 2px 0 0 171px;
    text-align: left;
  }
</style>
</head>
<body>
  <div class="card">
    <div class="brand-square" aria-hidden="true"></div>
    <div class="brand-name">VARELA</div>
    <div class="brand-tagline">Traumatologia Esportiva</div>

    <div class="stripe stripe--1"></div>
    <div class="stripe stripe--2"></div>

    <div class="name-band">
      <p>Dr. Luciano Varela</p>
      <p>CRM 584-902</p>
      <p>Cirurgia do Joelho/Esporte</p>
    </div>

    <div class="stripe stripe--3"></div>
    <div class="stripe stripe--4"></div>

    <div class="contact">
      <p>Centro Executivo - Pinheiral Plaza</p>
      <p>Av. Doutor Augusto Brandão Cunha, 2740 sala 0836</p>
      <p>Jd. Ipanema - Ribeirão Preto - SP</p>
      <p class="contact__web">
        <span>drlucianovarela@mailbox-exemplo.com</span>
        <span>www.drlucianovarela.com</span>
      </p>
      <div class="contact__phones">
        <span>Phone number</span><span>: Tel (16) 8245-3908</span>
        <span>Clinic phone</span><span>: (16) 3670-4851</span>
      </div>
    </div>
  </div>
</body>
</html>
```